Veterinary Clinic Letterhead - Ridgeview Veterinary Surgery

We need a letterhead design for an established Veterinary Clinic in Mareeba called Ridgeview Veterinary Surgery. We are a moderate sized mixed animal veterinary clinic offering a wide variety of veterinary services. The design should use the same colour pattern as those in the logos supplied. The design should also include our address (48 Tulloch Road, Tallowood, Westmere, 4790), phone number (07 4158 6734), email (admin@ridgeviewvets.com.au), website (www.ridgeviewvets.com.au) and our opening hours (8am to 5pm Monday to Friday and 8am to 12pm Saturday).
Target Market(s)
Pet owners
Industry/Entity Type
Veterinary
Requirements
Must have
- The logo or modification of it, business address, opening hours, website, phone number and email address

```html
<!DOCTYPE html>
<html lang="en">
<head>
<meta charset="utf-8">
<title>Ridgeview Veterinary Surgery – Letterhead</title>
<link href="https://fonts.googleapis.com/css2?family=Arimo:wght@400&family=Inter:wght@400;500;600&family=Montserrat:wght@500&display=swap" rel="stylesheet">
<style>
  :root {
    --navy: #002a4d;
    --ink: #2b2b2b;
    --body: #5a5a5a;
    --rule: #2d5b8f;
    --backdrop: #d9d9db;
    --paper-top: #ffffff;
    --paper-bottom: #dedede;
  }
  * { box-sizing: border-box; margin: 0; padding: 0; }
  html, body {
    width: 1039px; height: 1200px; overflow: hidden;
    background: var(--backdrop);
  }
  .letterhead {
    position: absolute; left: 93px; top: 0;
    width: 1184px; height: 1667px;
    transform: scale(0.72); transform-origin: top left;
    background: linear-gradient(160deg, var(--paper-top) 20%, var(--paper-bottom) 100%);
    overflow: hidden;
    font-family: "Inter", sans-serif;
  }
  .side-band { position: absolute; inset: 0; width: 1184px; height: 1667px; }

  .brand {
    position: absolute; left: 140px; top: 86px; width: 240px;
    text-align: center;
  }
  .brand-mark {
    width: 104px; height: 104px; border-radius: 50%;
    background: var(--navy); margin: 0 auto 14px;
  }
  .brand-name {
    font-family: "Montserrat", sans-serif; font-weight: 500;
    font-size: 17px; letter-spacing: 0.5px; line-height: 20px;
    color: var(--navy); text-transform: uppercase;
  }

  .divider {
    position: absolute; top: 153px; width: 2px; height: 78px;
    background: var(--rule);
  }
  .divider.one { left: 433px; }
  .divider.two { left: 757px; }

  .contact {
    position: absolute; font-size: 20px; line-height: 25.5px; color: var(--ink);
  }
  .contact.address { left: 485px; top: 152px; }
  .contact.reach { left: 810px; top: 150px; }
  .contact-row { display: flex; align-items: center; gap: 10px; }
  .contact .icon { width: 18px; height: 18px; flex: none; fill: var(--navy); }
  .address .lines { padding-left: 28px; margin-top: -25.5px; }

  .letter {
    position: absolute; left: 89px; top: 560px; width: 1000px;
    font-family: "Arimo", sans-serif; color: var(--body);
  }
  .salutation { font-size: 24px; margin-bottom: 28px; color: #555; }
  .letter p {
    font-size: 18px; line-height: 28px; text-align: justify;
    letter-spacing: 0.12px;
    margin-bottom: 28px; hyphens: auto;
  }
  .letter p.closing { margin-bottom: 0; }
  .signature {
    width: 150px; height: 62px; margin-top: 20px;
    background: linear-gradient(90deg, rgba(40,40,50,.14), rgba(40,40,50,.03));
    border-radius: 4px;
  }

  .hours {
    position: absolute; left: 0; right: 0; top: 1574px;
    text-align: center; font-size: 20px; color: #1e1e1e;
  }
  .hours strong { color: var(--navy); font-weight: 600; }
</style>
</head>
<body>
  <div class="letterhead">
    <svg class="side-band" viewBox="0 0 1184 1667" aria-hidden="true">
      <path d="M0 0 H155 C70 300 0 650 22 950 C40 1250 85 1500 122 1667 H0 Z" fill="var(--navy)"/>
      <path d="M172 0 C87 300 17 650 39 950 C57 1250 102 1500 138 1667" fill="none" stroke="var(--navy)" stroke-width="7"/>
    </svg>

    <div class="brand">
      <div class="brand-mark"></div>
      <div class="brand-name">Ridgeview Veterinary<br>Surgery</div>
    </div>

    <div class="divider one"></div>
    <div class="divider two"></div>

    <div class="contact address">
      <div class="contact-row">
        <svg class="icon" viewBox="0 0 24 24"><path d="M12 1C7.6 1 4 4.6 4 9c0 6 8 14 8 14s8-8 8-14c0-4.4-3.6-8-8-8zm0 11a3 3 0 1 1 0-6 3 3 0 0 1 0 6z"/></svg>
      </div>
      <div class="lines">48 Tulloch Road<br>Tallowood,<br>Westmere, 4790</div>
    </div>

    <div class="contact reach">
      <div class="contact-row">
        <svg class="icon" viewBox="0 0 24 24"><path d="M6.6 10.8a15 15 0 0 0 6.6 6.6l2.2-2.2a1 1 0 0 1 1-.25 11.4 11.4 0 0 0 3.6.6 1 1 0 0 1 1 1V20a1 1 0 0 1-1 1A17 17 0 0 1 3 4a1 1 0 0 1 1-1h3.5a1 1 0 0 1 1 1c0 1.25.2 2.45.57 3.57a1 1 0 0 1-.25 1z"/></svg>
        <span>(07 4158 6734)</span>
      </div>
      <div class="contact-row">
        <svg class="icon" viewBox="0 0 24 24"><path d="M2 5h20v14H2z M2 5l10 8 10-8" fill="var(--navy)" stroke="#fff" stroke-width="1.5"/></svg>
        <span>admin@ridgeviewvets.com.au</span>
      </div>
      <div class="contact-row">
        <svg class="icon" viewBox="0 0 24 24"><g fill="none" stroke="#555" stroke-width="1.6"><circle cx="12" cy="12" r="9.5"/><ellipse cx="12" cy="12" rx="4" ry="9.5"/><path d="M2.5 12h19M4 7h16M4 17h16"/></g></svg>
        <span>www.ridgeviewvets.com.au</span>
      </div>
    </div>

    <div class="letter">
      <div class="salutation">Dear Mr. Harper,</div>
      <p>Lorem ipsum dolor sit amet, consectetur adipiscing elit. Donec orci purus, luctus vitae dignissim eu, iaculis sed purus. Vivamus faucibus, ipsum nec aliquet viverra, leo mauris condimentum ligula, sit amet sagittis enim ligula quis arcu. Nam egestas tortor id nisi porttitor mattis. In tortor ante, ultricies in suscipit a, tempus non massa. Vivamus et auctor mi. Fusce vel massa nulla. Phasellus nec eros mauris, et scelerisque orci.</p>
      <p>Donec malesuada orci vitae nulla accumsan porta a id massa. Quisque accumsan iaculis magna sit amet fringilla. Maecenas consequat, magna eget tincidunt semper, odio nibh rutrum mi, id feugiat ante nisi eu risus. Vestibulum nunc orci, rhoncus a placerat in, ultricies in mi. Cras mattis varius eros, vel fringilla nisi suscipit eget. Quisque scelerisque sagittis nulla at porttitor.</p>
      <p>Sed id augue vitae urna euismod commodo aliquet a quam. Pellentesque arcu velit, cursus et malesuada ut, consequat et diam. Nullam erat sem, rhoncus id ullamcorper vitae, rhoncus et arcu. In ultricies ultricies nulla, ut rutrum nisi iaculis at. Donec eu magna a metus ornare faucibus. Fusce aliquet faucibus ultricies. Morbi semper, est id tincidunt gravida, sem arcu adipiscing lacus, ac bibendum nulla leo eu purus. Quisque nec diam sed risus consectetur a ccumsan quis quis nibh. Vestibulum id purus lorem.</p>
      <p class="closing">Sincerely,</p>
      <div class="signature" role="img" aria-label="Handwritten signature of the sender"></div>
    </div>

    <div class="hours"><strong>Monday to Friday</strong> - 8am to 5pm <strong>Saturday</strong> - 8am to 12pm</div>
  </div>
</body>
</html>
```